We are starting a new service that will combine local city menus and specials from local restaurants that will then be emailed and printed out on our website.. its a free service to the subscribers and a small charge to the restaurants. We need something to reflect the restaurant industry and to appeal to the general public alike, free to the end user. They sign up and receive daily specials in an email from our site.. not just one city but any one they pick that we service.. We would need links to include. Home, About Us, Sign Up (for free to public), Add Your Restaurant (increase sales and reduce daily calls).. and Contact Us link.. the name of the service is Town Plates in Motion and website will be townplatesinmotion.example. thank you

```html
<!DOCTYPE html>
<html lang="en">
<head>
<meta charset="utf-8">
<title>Town Plates in Motion</title>
<link href="https://fonts.googleapis.com/css2?family=Exo:wght@400;500;600&family=Open+Sans:wght@400;600;700&display=swap" rel="stylesheet">
<style>
:root{
  --brand:#e63a0f;
  --brand-dark:#c92f08;
  --ink:#3a3a3a;
  --muted:#9b9b9b;
  --page:#f1f1f1;
  --card:#ffffff;
  --bar:#2c2c2c;
  --line:#e4e4e4;
}
*{box-sizing:border-box;margin:0;padding:0}
html,body{width:1200px;height:2365px;overflow:hidden}
body{position:relative;background:var(--page);font-family:"Open Sans",Arial,sans-serif;color:var(--ink)}
.abs{position:absolute}
h1,h2,h3,h4{font-weight:400;font-family:"Exo",Arial,sans-serif}

/* header */
.site-header{left:0;top:0;width:1200px;height:120px;background:#fff;border-top:2px solid var(--brand)}
.brand{left:76px;top:0;width:160px;height:120px;background:var(--brand);display:flex;flex-direction:column;align-items:center;justify-content:center;color:#fff;font-family:"Exo",sans-serif;font-weight:500;font-size:19px;line-height:22px;text-align:center}
.drop-tab{left:583px;top:0;width:32px;height:16px;background:var(--brand)}
.support{right:70px;top:18px;font-size:13px;font-weight:600;color:var(--brand)}
.support span{color:var(--ink);font-weight:400}
.search{left:1167px;top:11px;width:33px;height:32px;background:var(--brand)}
.main-nav{left:552px;top:54px;height:66px;display:flex;border-left:1px solid var(--line)}
.main-nav a{display:flex;align-items:center;justify-content:center;height:66px;border-right:1px solid var(--line);font-size:12px;font-weight:600;color:var(--ink);text-decoration:none;letter-spacing:.2px}
.main-nav a.active{color:var(--brand)}

/* hero */
.hero{left:0;top:120px;width:1200px;height:479px;background:radial-gradient(ellipse at 62% 85%,#c7a06a 0%,#6e4c2c 28%,#2a1c14 55%,#0c0a09 100%)}
.hero-headline{left:568px;top:246px;width:553px;height:120px;background:rgba(20,20,20,.72);padding:22px 20px;color:#fff;font-family:"Exo",sans-serif;font-size:35px;line-height:40px;font-weight:500}
.hero-band{left:568px;top:378px;width:504px;height:46px;background:var(--brand);color:#fff;font-family:"Exo",sans-serif;font-weight:600;font-size:19px;line-height:46px;padding-left:20px}
.hero-btn{left:568px;top:459px;width:150px;height:35px;background:#fff;font-size:13px;font-weight:600;line-height:35px;text-align:center;color:var(--ink)}
.hero-arrow{top:345px}

/* features */
.feature{top:588px;width:260px;height:245px;background:var(--card);border-top:2px solid var(--brand);text-align:center}
.feature .icon{position:absolute;left:103px;top:-29px;width:54px;height:54px;border-radius:50%;background:var(--brand);display:flex;align-items:center;justify-content:center}
.feature h3{margin-top:44px;font-size:25px;color:#555}
.feature.hot h3{color:var(--brand)}
.feature p{margin:18px auto 0;width:220px;font-size:12px;line-height:20px}
.btn-grey{display:inline-block;margin-top:28px;width:110px;height:33px;line-height:33px;font-size:10px;font-weight:600;background:linear-gradient(#f4f4f4,#d9d9d9);color:#555;border-radius:2px}
.feature.hot .btn-grey{background:var(--brand);color:#fff}

/* tile grids */
.tiles{left:76px;width:1047px;height:523px;display:grid;grid-template-columns:repeat(4,1fr);grid-template-rows:repeat(2,1fr)}
.tile{position:relative;background:var(--card);padding:30px 26px}
.tile h3{font-size:25px;line-height:28px;color:var(--muted)}
.tile h4{font-family:"Open Sans",sans-serif;font-size:11px;font-weight:700;margin-top:18px;line-height:16px;color:#333}
.tile p{font-size:12px;line-height:20px;margin-top:14px}
.photo{position:relative}
.notch-l::before,.notch-b::before{content:"";position:absolute;width:0;height:0;border:10px solid transparent;z-index:2}
.notch-l::before{left:-10px;top:60px;border-left:0;border-right-color:var(--card)}
.notch-b::before{left:120px;bottom:-10px;border-bottom:0;border-top-color:var(--card)}
.span2{grid-row:1 / span 2}
.accent{background:var(--brand);color:#fff;padding:30px 28px}
.accent h2{font-size:34px;line-height:36px;font-weight:500}
.dots{display:flex;gap:6px;margin:18px 0 16px}
.dots i{width:8px;height:8px;border-radius:50%;background:rgba(255,255,255,.6)}
.dots i:first-child{background:#fff}
.accent p{font-size:12px;line-height:20.5px}
.btn-white{display:inline-block;margin-top:20px;width:188px;height:34px;line-height:34px;text-align:center;background:#fff;color:#333;font-size:12px;font-weight:600;border-radius:2px}
.photo-ui{position:absolute;left:106px;top:70px}
.photo-ui .rm{width:84px;height:26px;background:var(--brand);color:#fff;font-size:10px;font-weight:700;line-height:26px;text-align:center}
.photo-ui .sq{display:inline-block;width:32px;height:32px;margin:8px 4px 0 0;background:#fff}
.photo-ui .sq.red{background:var(--brand)}

.to-top{left:1126px;top:1541px;width:30px;height:31px;background:var(--brand)}

/* footer */
.social-bar{left:0;top:2012px;width:1200px;height:34px;background:var(--bar);border-bottom:2px solid var(--brand)}
.social{left:485px;top:9px;display:flex;gap:14px}
.social i{width:16px;height:16px;border-radius:50%;background:#e6e6e6}
.collapse{left:1093px;top:0;width:30px;height:34px;background:var(--brand)}
.footer-col{top:2076px;width:230px}
.footer-col h3{font-size:27px;color:#555;margin-bottom:18px}
.footer-col .f-brand{color:var(--brand);font-family:"Exo",sans-serif;font-weight:500;font-size:27px;margin-bottom:18px}
.footer-col p{font-size:12px;line-height:20.5px}
.tweet{font-size:11px;line-height:17px;margin-bottom:18px;padding-left:14px;position:relative}
.tweet::before{content:"";position:absolute;left:0;top:5px;width:8px;height:8px;border-radius:50%;background:#333}
.tweet small{display:block;color:var(--muted);font-size:10px}
.features-list{list-style:none}
.features-list li{font-size:11px;line-height:29px;display:flex;align-items:center;gap:8px}
.features-list svg{flex:none}
.thumbs{display:grid;grid-template-columns:repeat(3,70px);gap:7px}
.thumbs div{height:70px}
.bottom-bar{left:0;top:2331px;width:1200px;height:34px;background:var(--bar);color:#ddd;font-size:11px;line-height:34px}
.bottom-bar .copy{position:absolute;left:76px}
.bottom-bar nav{position:absolute;right:77px}
.bottom-bar nav a{color:#ddd;text-decoration:none;margin-left:4px}
.bottom-bar nav a.active{color:var(--brand)}
.bottom-bar nav b{color:var(--brand);font-weight:400}
</style>
</head>
<body>

<header class="site-header abs">
  <div class="brand abs">Town Plates<br>in Motion</div>
  <div class="drop-tab abs"><svg width="32" height="16"><path d="M11 5l5 5 5-5" fill="none" stroke="#fff" stroke-width="2"/></svg></div>
  <div class="support abs">CUSTOMER SUPPORT 24/7: <span>+44 100 555 0199</span></div>
  <div class="search abs"><svg width="33" height="32"><circle cx="15" cy="14" r="6" fill="none" stroke="#fff" stroke-width="2.5"/><path d="M19.5 18.5l5 5" stroke="#fff" stroke-width="3"/></svg></div>
  <nav class="main-nav abs">
    <a class="active" style="width:91px">HOME</a>
    <a style="width:106px">ABOUT US</a>
    <a style="width:92px">SIGN UP</a>
    <a style="width:171px">ADD YOUR RESTAURANT</a>
    <a style="width:111px">CONTACTS US</a>
  </nav>
</header>

<section class="hero abs" role="img" aria-label="Woman checking restaurant menus on her phone beside a plated dish">
</section>
<svg class="hero-arrow abs" style="left:20px" width="20" height="34"><path d="M16 2L4 17l12 15" fill="none" stroke="#777" stroke-width="2"/></svg>
<svg class="hero-arrow abs" style="left:1160px" width="20" height="34"><path d="M4 2l12 15L4 32" fill="none" stroke="#777" stroke-width="2"/></svg>
<h1 class="hero-headline abs">GREAT MENUS ON THE GO AT<br>YOUR GINGER-SRTIPS.</h1>
<div class="hero-band abs">SUBSCRIBE NOW TO GET ALERT ON NEW LISTING.</div>
<div class="hero-btn abs">JOIN US TODAY</div>

<article class="feature abs" style="left:76px">
  <div class="icon"><svg width="26" height="24"><path d="M13 22L3 12a5.5 5.5 0 0 1 10-7 5.5 5.5 0 0 1 10 7z" fill="#fff"/></svg></div>
  <h3>MADE WITH LOVE</h3>
  <p>Lorem ipsum dolor sit amet, consectetur adipiscing elit, sed do eiusmod tempor incididunt ut labore.</p>
  <span class="btn-grey">LEARN MORE</span>
</article>
<article class="feature abs" style="left:339px">
  <div class="icon"><svg width="28" height="24"><circle cx="14" cy="12" r="8" fill="#fff"/><path d="M2 3v18M26 3v18" stroke="#fff" stroke-width="2"/></svg></div>
  <h3>TRENDY MENU</h3>
  <p>Lorem ipsum dolor sit amet, consectetur adipiscing elit, sed do eiusmod tempor incididunt ut labore.</p>
  <span class="btn-grey">LEARN MORE</span>
</article>
<article class="feature hot abs" style="left:602px">
  <div class="icon"><svg width="28" height="20"><rect x="1" y="1" width="26" height="18" fill="none" stroke="#fff" stroke-width="2"/><path d="M1 2l13 10 13-10" fill="none" stroke="#fff" stroke-width="2"/></svg></div>
  <h3>DAILY UPDATES</h3>
  <p>Lorem ipsum dolor sit amet, consectetur adipiscing elit, sed do eiusmod tempor incididunt ut labore.</p>
  <span class="btn-grey">LEARN MORE</span>
</article>
<article class="feature abs" style="left:864px">
  <div class="icon"><svg width="26" height="26"><circle cx="13" cy="13" r="11" fill="none" stroke="#fff" stroke-width="2"/><ellipse cx="13" cy="13" rx="4.5" ry="11" fill="none" stroke="#fff" stroke-width="1.5"/><path d="M2 13h22" stroke="#fff" stroke-width="1.5"/></svg></div>
  <h3>RENOWNED SHOP</h3>
  <p>Lorem ipsum dolor sit amet, consectetur adipiscing elit, sed do eiusmod tempor incididunt ut labore.</p>
  <span class="btn-grey">LEARN MORE</span>
</article>

<section class="tiles abs" style="top:877px">
  <div class="photo" role="img" aria-label="Plate of grilled prawns in sauce" style="background:linear-gradient(135deg,#8e1c1c,#c7622a 55%,#7a1414)">
    <div class="photo-ui"><div class="rm">READ MORE</div><span class="sq"></span><span class="sq red"></span></div>
  </div>
  <div class="tile notch-l">
    <h3>MENU TITLE<br>NARRATE HERE</h3>
    <p>Lorem ipsum dolor sit amet, consectetur adipiscing elit. Nam vel turpis. Duis sit amet lectus ac mauris porta viverra. Aliquam erat volutpat. Praesent ipsum pede [..]</p>
  </div>
  <div class="photo" role="img" aria-label="Grilled steak with vegetables and a gravy boat" style="background:linear-gradient(160deg,#d9c7a3,#9a4a2a 55%,#5a2a1a)"></div>
  <div class="tile accent span2">
    <h2>LATEST CITY<br>MENUS</h2>
    <div class="dots"><i></i><i></i><i></i></div>
    <p>Lorem ipsum dolor sit amet, consectetur adipiscing elit. Nam vel turpis. Duis sit amet lectus ac mauris porta viverra. Aliquam erat volutpat. Praesent ipsum pede, pretium sed, congue nec, pretium quis, urna. Lorem ipsum dolor sit amet, consectetur adipiscing elit. Nam vel turpis. Duis sit amet lectus ac mauris porta viverra. Aliquam erat volutpat. Praesent ipsum pede...</p>
    <span class="btn-white">SUBSCRIBE NOW</span>
  </div>
  <div class="tile notch-b" style="grid-row:2">
    <h3>MENU TITLE<br>NARRATE HERE</h3>
    <h4>LOOKING FOR QUALITY SALAD RECIPES?</h4>
    <p>Lorem ipsum dolor sit amet, consectetur adipiscing elit. Nam vel turpis. Duis sit amet lectus [..]</p>
  </div>
  <div class="photo" role="img" aria-label="Glasses of tomato salad skewers on a table" style="grid-row:2;background:linear-gradient(160deg,#efe9e6,#c9b7b2 50%,#b33a2a)"></div>
  <div class="tile notch-l" style="grid-row:2">
    <h3>MENU TITLE<br>NARRATE HERE</h3>
    <h4>LOOKING FOR FRESH STRAWBERRY TASTE?</h4>
    <p>Lorem ipsum dolor sit amet, consectetur adipiscing elit. Nam vel turpis. Duis sit amet lectus [..]</p>
  </div>
</section>

<section class="tiles abs" style="top:1444px">
  <div class="tile accent span2">
    <h2>FIND CITY<br>RESTAURANT</h2>
    <div class="dots"><i></i><i></i><i></i></div>
    <p>Lorem ipsum dolor sit amet, consectetur adipiscing elit. Nam vel turpis. Duis sit amet lectus ac mauris porta viverra. Aliquam erat volutpat. Praesent ipsum pede, pretium sed, congue nec, pretium quis, urna. Lorem ipsum dolor sit amet, consectetur adipiscing elit. Nam vel turpis. Duis sit amet lectus ac mauris porta viverra. Aliquam erat volutpat. Praesent ipsum pede...</p>
    <span class="btn-white">ADD YOUR RESTAURANT</span>
  </div>
  <div class="tile notch-b">
    <h3>NAME OF<br>RESTAURANT</h3>
    <h4>NEW YORK</h4>
    <p>Print some favourite menus of the restaurant to quicly overview &nbsp;what the customers can find there before going to the place...</p>
  </div>
  <div class="photo" role="img" aria-label="Couple dining with wine at a restaurant" style="background:linear-gradient(160deg,#8a5a32,#d8b48a 50%,#5a3a22)"></div>
  <div class="tile notch-l">
    <h3>NAME OF<br>RESTAURANT</h3>
    <h4>CHICAGO</h4>
    <p>Print some favourite menus of the restaurant to quicly overview &nbsp;what the customers can find there before going to the place...</p>
  </div>
  <div class="photo" role="img" aria-label="Outdoor restaurant terrace with set tables" style="grid-row:2;background:linear-gradient(170deg,#6c8a3a,#c9c2b0 55%,#2e2a26)"></div>
  <div class="tile notch-l" style="grid-row:2">
    <h3>NAME OF<br>RESTAURANT</h3>
    <h4>WASHINGTON D.C.</h4>
    <p>Print some favourite menus of the restaurant to quicly overview &nbsp;what the customers can find there before going to the place...</p>
  </div>
  <div class="photo notch-l" role="img" aria-label="Chefs at work in a restaurant kitchen" style="grid-row:2;background:linear-gradient(160deg,#8d8f92,#e8e6e2 50%,#6a6460)"></div>
</section>

<div class="to-top abs"><svg width="30" height="31"><path d="M9 18l6-6 6 6" fill="none" stroke="#fff" stroke-width="2"/></svg></div>

<div class="social-bar abs">
  <div class="social abs"><i></i><i></i><i></i><i></i><i></i><i></i><i></i></div>
  <div class="collapse abs"><svg width="30" height="34"><path d="M9 17h12" stroke="#fff" stroke-width="3"/></svg></div>
</div>

<div class="footer-col abs" style="left:76px">
  <div class="f-brand">Town Plates in Motion</div>
  <p>Lorem ipsum ex vix illud nonummy, novum tation et his. At vix scriptaset Lorem ipsum ex vix illud nonummy, novum tation et his. At vix scriptaset patrioque scribentur, at pro fugit erts verterem molestiae, sed et vivendo ali Lorem ipsum ex vix illud nonummy, novum tation et his...</p>
</div>
<div class="footer-col abs" style="left:339px">
  <h3>TWEETS</h3>
  <div class="tweet">I liked a @PlateFeed video lnk.example/9dAfsfbdfds321 Lorem ipsum<small>ABOUT 1 DAY AGO</small></div>
  <div class="tweet">I liked a @PlateFeed video lnk.example/9d42<small>ABOUT 1 DAY AGO</small></div>
  <div class="tweet">I liked a @ForkLane pen lnk.example/9D<small>ABOUT 1 DAY AGO</small></div>
</div>
<div class="footer-col abs" style="left:598px">
  <h3>GREAT FEATURES</h3>
  <ul class="features-list">
    <li><svg width="10" height="10"><path d="M1 5l3 3 5-7" fill="none" stroke="#e63a0f" stroke-width="2"/></svg>Anytime access to your fav menus</li>
    <li><svg width="10" height="10"><path d="M5 0l1.5 3.5L10 4 7.3 6.3 8 10 5 8 2 10l.7-3.7L0 4l3.5-.5z" fill="#e63a0f"/></svg>Instance help on your queries</li>
    <li><svg width="10" height="10"><rect x="1" y="1" width="8" height="8" fill="#e63a0f"/></svg>Lot of restaurants approach</li>
    <li><svg width="10" height="10"><path d="M5 9L1 5a2.3 2.3 0 0 1 4-3 2.3 2.3 0 0 1 4 3z" fill="#e63a0f"/></svg>Trendy &amp; delicious items</li>
    <li><svg width="10" height="10"><path d="M1 5h8" stroke="#e63a0f" stroke-width="2"/></svg>Reduce time consuming</li>
    <li><svg width="10" height="10"><path d="M1 5h7M5 2l3 3-3 3" fill="none" stroke="#e63a0f" stroke-width="1.6"/></svg>Build new business for your shop</li>
  </ul>
</div>
<div class="footer-col abs" style="left:861px">
  <h3>RECENT PHOTOS</h3>
  <div class="thumbs">
    <div role="img" aria-label="Dish photo" style="background:#b8442e"></div>
    <div role="img" aria-label="Dish photo" style="background:#a8321c"></div>
    <div role="img" aria-label="Dish photo" style="background:#8a9a4a"></div>
    <div role="img" aria-label="Dish photo" style="background:#6a6e8a"></div>
    <div role="img" aria-label="Dish photo" style="background:#d6a03a"></div>
    <div role="img" aria-label="Dish photo" style="background:#7a8a5a"></div>
  </div>
</div>

<footer class="bottom-bar abs">
  <span class="copy">© COPYRIGHT 2014. TOWNPLATESINMOTION.EXAMPLE</span>
  <nav><b>·</b> <a class="active">HOME</a> <b>·</b> <a>ABOUT US</a> <b>·</b> <a>SIGN UP</a> <b>·</b> <a>ADD YOUR RESTAURANT</a> <b>·</b> <a>CONTACT US</a></nav>
</footer>

</body>
</html>
```